Discreet simple classy for adult entertainment

I would like a matte black business card with gold writing for my business. Keeping it simple. Having my following:

Lana frost
Events. Entertainment. Promotions
0491726580

or alternatively could have what i had on my previous card below but i think i prefer the above as again - discretion.

Maybe a nice gold line thru the card or some other very simple design . Or not open to ideas/ can be doublesided if any good ideas with that.

included pics of my old bus card. not sure weather i want a photo on it or not. if i do it wont be the same pic. i kinda wanted a card that was discreet so if it was in someones wallet they wouldn't neccessarily realise it was from a stripper.

Target Market(s)

men

Industry/Entity Type

Business

Contact Information for Business Card

Lana frost
0491726580

Requirements
Nice to have
• i don't know i am really open to anything. im giving my cards to guys so something they can have in their wallet that is discreet preferably.

```html
<!DOCTYPE html>
<html lang="en">
<head>
<meta charset="utf-8">
<title>Lana Frost — Business Card</title>
<link rel="stylesheet" href="https://fonts.googleapis.com/css2?family=Orbitron:wght@600&family=Lato:wght@400&display=swap">
<style>
  :root {
    --backdrop: #e7e4e2;
    --card: #f6f4f3;
    --card-edge: #dcd8d5;
    --band: #ffd800;
    --band-line: #b79a00;
    --ink: #141414;
  }
  html, body {
    margin: 0;
    width: 1200px;
    height: 900px;
    overflow: hidden;
    background: var(--backdrop);
  }
  .canvas {
    position: relative;
    width: 1200px;
    height: 900px;
  }
  .card {
    position: absolute;
    width: 556px;
    height: 342px;
    background: var(--card);
    border: 1px solid var(--card-edge);
    box-sizing: border-box;
  }
  .card--front { left: 238px; top: 62px; }
  .card--back  { left: 460px; top: 518px; width: 560px; }
  .band {
    position: absolute;
    left: 0;
    right: 0;
    top: 102px;
    height: 139px;
    background: var(--band);
    overflow: hidden;
  }
  .band__lines {
    position: absolute;
    inset: 0;
    width: 100%;
    height: 100%;
  }
  .band__lines line {
    stroke: var(--band-line);
    stroke-width: 1;
  }
  .band__content {
    position: relative;
    height: 100%;
    display: flex;
    flex-direction: column;
    align-items: center;
    justify-content: center;
    color: var(--ink);
  }
  .card__name {
    margin: 0;
    font-family: "Orbitron", sans-serif;
    font-weight: 600;
    font-size: 31px;
    letter-spacing: 2px;
    text-transform: uppercase;
    line-height: 1;
    margin-top: -8px;
  }
  .card__phone {
    margin: 18px 0 0;
    font-family: "Lato", sans-serif;
    font-size: 20px;
    letter-spacing: 0.5px;
  }
  .card__tagline {
    margin: 0;
    font-family: "Lato", sans-serif;
    font-size: 17px;
  }
</style>
</head>
<body>
<main class="canvas">
  <section class="card card--front" aria-label="Card front">
    <div class="band">
      <svg class="band__lines" viewBox="0 0 556 139" preserveAspectRatio="none" aria-hidden="true">
        <line x1="150" y1="0" x2="7" y2="139"/>
        <line x1="556" y1="16" x2="422" y2="139"/>
      </svg>
      <div class="band__content">
        <h1 class="card__name">Lana Frost</h1>
        <p class="card__phone">0491726580</p>
      </div>
    </div>
  </section>

  <section class="card card--back" aria-label="Card back">
    <div class="band">
      <svg class="band__lines" viewBox="0 0 560 139" preserveAspectRatio="none" aria-hidden="true">
        <line x1="150" y1="0" x2="10" y2="139"/>
        <line x1="560" y1="8" x2="426" y2="139"/>
      </svg>
      <div class="band__content">
        <p class="card__tagline">Events. Entertainment. Promotions</p>
      </div>
    </div>
  </section>
</main>
</body>
</html>
```